Progressive Architecture and Urban Planning Studio - Stationery Design

The Kestrel Collective: a small boutique Architectural and Urban Planning Studio based in Natal/ RN, Brazil, about to open branches in South Africa and West Africa, established to provide high quality, innovative design and personal client service for projects worldwide. Our approach to Architecture: Minimal - Less is More, so to speak, but with an edge! Strive to produce "clean" projects - stripped of all that can be stripped, no excesses. Got our Logo right here with Pixel Harbor, and hope to do the same with our stationery (were informed that includes business cards, letterhead and envelopes). Since we'll be using two clour schemes, we want at least one using a black background (business card). We'll also allow manipulation of our logo if it helps the final design. Good Luck!

Font styles to use
Other font styles liked:
• Nexa

Colors

Designer to choose colors to be used in the design.

Requirements
Must have
• Business Cards/ Letterheads with the following address:
Rua Olavo Pereira 2741, Vale Dourado, Natal/RN
Should be able to edit it.

```html
<!DOCTYPE html>
<html lang="en">
<head>
<meta charset="utf-8">
<title>The Kestrel Collective – Stationery</title>
<link href="https://fonts.googleapis.com/css2?family=Questrial&display=swap" rel="stylesheet">
<style>
  :root {
    --backdrop: #2b2b2b;
    --paper: #f2f2f1;
    --card-light: #e9e9e9;
    --ink-dark: #3a3a3a;
    --black: #0b0b0b;
    --black-flap: #161616;
    --white: #ffffff;
    --accent-red: #e0262b;
  }
  * { box-sizing: border-box; margin: 0; padding: 0; }
  html, body {
    width: 1200px;
    height: 900px;
    overflow: hidden;
    background: var(--backdrop);
    font-family: "Questrial", "Helvetica Neue", Arial, sans-serif;
  }
  .canvas { position: relative; width: 1200px; height: 900px; }

  .brand {
    display: flex;
    align-items: center;
    gap: 0.55em;
    letter-spacing: 0.12em;
    text-transform: uppercase;
    white-space: nowrap;
  }
  .brand-square {
    display: inline-block;
    width: 1em;
    height: 1em;
    background: var(--accent-red);
    flex: none;
  }
  .address { white-space: nowrap; }

  /* Letterhead */
  .letterhead {
    position: absolute;
    left: 22px; top: 68px;
    width: 546px; height: 778px;
    background: var(--paper);
  }
  .letterhead .brand {
    position: absolute; left: 14px; top: 9px;
    font-size: 9px; color: var(--ink-dark);
  }
  .letterhead .address {
    position: absolute; left: 11px; top: 34px;
    font-size: 5px; color: var(--ink-dark);
  }

  /* Light business card */
  .card-light {
    position: absolute;
    left: 595px; top: 346px;
    width: 230px; height: 125px;
    background: var(--card-light);
    display: flex; flex-direction: column;
    align-items: center; justify-content: center;
    gap: 10px;
  }
  .card-light .brand { font-size: 9px; color: var(--ink-dark); }
  .card-light .address { font-size: 6px; color: var(--ink-dark); }

  /* Dark business card */
  .card-dark {
    position: absolute;
    left: 831px; top: 299px;
    width: 362px; height: 202px;
    background: var(--black);
    display: flex; flex-direction: column;
    align-items: center; justify-content: center;
    gap: 18px;
  }
  .card-dark .brand { font-size: 15px; color: var(--white); }
  .card-dark .address { font-size: 10px; color: var(--white); }

  /* Envelope */
  .envelope {
    position: absolute;
    left: 638px; top: 588px;
    width: 458px; height: 228px;
    background: var(--black);
  }
  .envelope-flap {
    height: 50px;
    background: var(--black-flap);
    border-bottom: 1px solid #242424;
    display: flex; align-items: center;
    padding-left: 18px;
  }
  .envelope .brand { font-size: 10px; color: var(--white); }
</style>
</head>
<body>
<main class="canvas">

  <section class="letterhead" aria-label="Letterhead">
    <div class="brand"><span class="brand-square"></span>The Kestrel Collective</div>
    <p class="address">Rua Olavo Pereira 2741, Vale Dourado, Natal/RN</p>
  </section>

  <section class="card-light" aria-label="Business card, light">
    <div class="brand"><span class="brand-square"></span>The Kestrel Collective</div>
    <p class="address">Rua Olavo Pereira 2741, Vale Dourado, Natal/RN</p>
  </section>

  <section class="card-dark" aria-label="Business card, black">
    <div class="brand"><span class="brand-square"></span>The Kestrel Collective</div>
    <p class="address">Rua Olavo Pereira 2741, Vale Dourado, Natal/RN</p>
  </section>

  <section class="envelope" aria-label="Envelope">
    <div class="envelope-flap">
      <div class="brand"><span class="brand-square"></span>The Kestrel Collective</div>
    </div>
  </section>

</main>
</body>
</html>
```